Welbourne Dental, P.C. New stationary and business card for modern Dental Office

We need a new stationary/envelope/business card design using our newly designed logo. We are looking for an upscale look. Our new logo is used on our signage, using black as the background and white for the lettering. We would like the stationary to have black, white, possible greys or silver. We are looking for a letterhead, envelope, and business card design for three different employees, as well as a 4th card, same design, but just general with no employee name.

Project Deadline Extended
Reason: We began this project in the middle of our move into our new office. Things got pretty hectic and we just didn't have the time to go through designs. We now settled in and finally eliminated the designs that didn't work for us. We would like to extend the project another 5 days, and then finalize our decision. Most of the submissions showed business cards alone, with no stationary designs. Our original request was for stationary and business cards. Please keep this in mind.

Target Market(s)

Dental patients expecting high quality, cosmetic dentistry

Industry/Entity Type

Business

Contact Information for Business Card

Will need a design using our logo. All cards will be the same, other than that one card will have Office Managers name, One for the Doctor, Hygienist,
1. Office Manager - Marisol Dubrovka
2. Hygienist - Kayleigh Morrow
3. Gordon T. Welbourne, D.D.S.
4. One general one with no staff names

Font styles to use
Other font styles liked:
• see upload

Colors
000000
1b1b1b
757575
c9c9c9
e8e8e8
ffffff

Requirements
Must have
• -Logo
• -Phone number (718)555-0193
• -Address: 4352 63rd Ave
• Lower Level
• Brooklyn, NY 11290

```html
<!DOCTYPE html>
<html lang="en">
<head>
<meta charset="utf-8">
<title>Welbourne Dental, P.C. — Stationery Set</title>
<link rel="stylesheet" href="https://fonts.googleapis.com/css2?family=Tinos:wght@400;700&family=Open+Sans:wght@400&display=swap">
<style>
  :root {
    --black: #000000;
    --ink: #1b1b1b;
    --grey: #757575;
    --silver: #c9c9c9;
    --mist: #e8e8e8;
    --paper: #ffffff;
  }
  * { box-sizing: border-box; margin: 0; padding: 0; }
  html, body { width: 1200px; height: 900px; overflow: hidden; }
  body {
    position: relative;
    background: var(--mist);
    font-family: "Tinos", "Times New Roman", serif;
    color: var(--ink);
  }
  .sheet {
    position: absolute;
    background: var(--paper);
    border: 1px solid var(--silver);
  }
  .address {
    position: absolute;
    font-weight: 700;
    line-height: 1.25;
    color: var(--black);
  }
  .rule-double {
    position: absolute;
    border-top: 1.5px solid var(--ink);
    border-bottom: 1.5px solid var(--ink);
  }
  .rule-double.vertical {
    border: none;
    border-left: 1.5px solid var(--ink);
    border-right: 1.5px solid var(--ink);
  }
  .wordmark {
    position: absolute;
    display: flex;
    align-items: center;
    gap: 6px;
    white-space: nowrap;
  }
  .wordmark-name {
    font-family: "Tinos", "Times New Roman", serif;
    font-weight: 400;
    color: var(--ink);
  }
  .wordmark-dot { display: block; }

  /* Envelope front */
  .envelope-front { left: 128px; top: 170px; width: 330px; height: 164px; }
  .envelope-front .address { left: 12px; top: 10px; font-size: 7px; }
  .envelope-front .rule-h { left: 64px; top: 13px; width: 118px; height: 4px; }
  .envelope-front .rule-v { left: 13px; top: 43px; width: 5px; height: 108px; }
  .envelope-front .wordmark { right: 12px; bottom: 30px; }
  .envelope-front .wordmark-name { font-size: 15px; }

  /* Envelope back */
  .envelope-back { left: 308px; top: 92px; width: 301px; height: 165px; overflow: hidden; }
  .envelope-back .flap { position: absolute; left: 0; top: 0; width: 100%; height: 52px; }
  .envelope-back .note {
    position: absolute; left: 30px; top: 122px; width: 240px;
    font-family: "Open Sans", Arial, sans-serif;
    font-size: 5.5px; line-height: 1.8; color: var(--grey);
  }

  /* Letterhead */
  .letterhead { left: 421px; top: 349px; width: 315px; height: 447px; }
  .letterhead .address { left: 22px; top: 43px; font-size: 7.5px; }
  .letterhead .rule-left { position: absolute; left: 22px; top: 79px; width: 105px; border-top: 1px solid var(--ink); }
  .letterhead .rule-mid { position: absolute; left: 133px; top: 79px; width: 55px; border-top: 1px solid var(--silver); }
  .letterhead .wordmark { right: 8px; top: 48px; }
  .letterhead .wordmark-name { font-size: 15px; }
  .letterhead .rule-foot { left: 16px; top: 390px; width: 283px; height: 6px; }

  /* Business card */
  .business-card { left: 762px; top: 350px; width: 135px; height: 68px; }
  .business-card .person { position: absolute; left: 4px; top: 19px; width: 60px; text-align: center; }
  .business-card .person-name { font-size: 7.5px; font-weight: 700; color: var(--black); }
  .business-card .person-title { font-size: 4.5px; font-style: italic; color: var(--grey); margin-top: 3px; }
  .business-card .email { position: absolute; left: 4px; top: 56px; width: 60px; text-align: center; font-size: 4.5px; font-weight: 700; }
  .business-card .rule-v { left: 63px; top: 5px; width: 4px; height: 59px; }
  .business-card .wordmark { left: 72px; top: 10px; gap: 3px; }
  .business-card .wordmark-name { font-size: 5.5px; }
  .business-card .address { left: 78px; top: 43px; font-size: 4.3px; font-weight: 400; }
</style>
</head>
<body>

  <section class="sheet envelope-front" aria-label="Envelope front">
    <p class="address">4352 63rd Ave<br>Lower Level<br>Brooklyn, NY 11290<br>(718)555-0193</p>
    <div class="rule-double rule-h"></div>
    <div class="rule-double vertical rule-v"></div>
    <div class="wordmark">
      <span class="wordmark-name">Welbourne Dental, P.C.</span>
      <svg class="wordmark-dot" width="12" height="12" viewBox="0 0 12 12"><circle cx="6" cy="6" r="5" fill="none" stroke="#1b1b1b" stroke-width="1.2"/></svg>
    </div>
  </section>

  <section class="sheet envelope-back" aria-label="Envelope back">
    <svg class="flap" viewBox="0 0 301 52" preserveAspectRatio="none"><polygon points="0,0 301,0 284,52 17,52" fill="#757575"/></svg>
    <p class="note">Nullam in mi felis. Mauris sit amet lobortis ex, a pellentesque nulla. Lorem ipsum dolor sit amet, consectetur adipiscing elit. Nunc velit urna.</p>
  </section>

  <section class="sheet letterhead" aria-label="Letterhead">
    <p class="address">4352 63rd Ave<br>Lower Level<br>Brooklyn, NY 11290<br>(718)555-0193</p>
    <div class="rule-left"></div>
    <div class="rule-mid"></div>
    <div class="wordmark">
      <span class="wordmark-name">Welbourne Dental, P.C.</span>
      <svg class="wordmark-dot" width="12" height="12" viewBox="0 0 12 12"><circle cx="6" cy="6" r="5" fill="none" stroke="#1b1b1b" stroke-width="1.2"/></svg>
    </div>
    <div class="rule-double rule-foot"></div>
  </section>

  <section class="sheet business-card" aria-label="Business card">
    <div class="person">
      <p class="person-name">Tobias Renner</p>
      <p class="person-title">Title</p>
    </div>
    <p class="email">tobias@welbourne.com</p>
    <div class="rule-double vertical rule-v"></div>
    <div class="wordmark">
      <span class="wordmark-name">Welbourne Dental, P.C.</span>
      <svg class="wordmark-dot" width="6" height="6" viewBox="0 0 12 12"><circle cx="6" cy="6" r="5" fill="none" stroke="#1b1b1b" stroke-width="1.4"/></svg>
    </div>
    <p class="address">4352 63rd Ave<br>Lower Level<br>Brooklyn, NY 11290<br>(718)555-0193</p>
  </section>

</body>
</html>
```